Mt Brindlewood Hotel

We need a business card with old world charm.
The design will need to promote dining and accommodation for local residents as a place to relax and for vacationing or week-end visitors seeking an experience of country hospitality.
The hotel was originally opened in 1909.

Target Market(s)

Adults and Families searching for dining and accommodation.

Industry/Entity Type

Business

Requirements
Nice to have
• Sketch or line drawing of Hotel

```html
<!DOCTYPE html>
<html lang="en">
<head>
<meta charset="utf-8">
<title>Mt Brindlewood Hotel — Business Card</title>
<link rel="stylesheet" href="https://fonts.googleapis.com/css2?family=Uncial+Antiqua&family=PT+Sans&display=swap">
<style>
  :root {
    --card-bg: #ffffff;
    --title-red: #ff4a0a;
    --contact-grey: #8c9c9b;
    --hotel-dark: #2e2e2e;
    --hotel-mid: #4a4a4a;
    --hotel-light: #8a8a8a;
  }
  html, body {
    margin: 0;
    padding: 0;
    overflow: hidden;
    background: var(--card-bg);
  }
  .card {
    position: relative;
    width: 1200px;
    height: 783px;
    background: var(--card-bg);
    overflow: hidden;
  }
  .hotel-name {
    position: absolute;
    right: 76px;
    top: 74px;
    margin: 0;
    font-family: "Uncial Antiqua", serif;
    font-weight: 400;
    font-size: 46px;
    line-height: 1;
    color: var(--title-red);
    text-transform: uppercase;
    word-spacing: 22px;
    white-space: nowrap;
  }
  .contact {
    position: absolute;
    right: 78px;
    top: 160px;
    margin: 0;
    font-family: "PT Sans", sans-serif;
    font-style: normal;
    font-size: 33px;
    line-height: 42px;
    color: var(--contact-grey);
    text-align: right;
    letter-spacing: 0.5px;
    white-space: nowrap;
  }
  .contact span { display: block; }
  .hotel-sketch {
    position: absolute;
    left: 78px;
    top: 428px;
    width: 539px;
    height: 278px;
    background: linear-gradient(180deg, var(--hotel-light) 0%, var(--hotel-mid) 30%, var(--hotel-dark) 100%);
  }
</style>
</head>
<body>
  <main class="card">
    <h1 class="hotel-name">Mt Brindlewood Hotel</h1>
    <address class="contact">
      <span>4821 Wattle Road</span>
      <span>Mt Brindlewood NSW 2000</span>
      <span>+61 4321 8765</span>
      <span>info@mtbrindlewoodhotel.com</span>
      <span>www.mtbrindlewoodhotel.com</span>
    </address>
    <div class="hotel-sketch" role="img" aria-label="Dark greyscale illustration of the historic two-storey hotel building with chimneys, gabled roof and verandah, beside a tree"></div>
  </main>
</body>
</html>
```